Verdane Clinical Spa needs an eye-catching poster to help promote our largest sale of spring!

We need a poster that will go on the back of the doors in the patient rooms. Our medical spa is professional and high-end, so we want the poster to look sophisticated, yet very eye-catching.
This project is for our Marigold Jubilee special, our second largest sale of the year.

Name: Marigold Jubilee
Slogan: Let Your Beauty Bloom
Sale: The More You Buy, The More You Save

Choose from your favorite spa services
NEVRIL, Laser Treatments, Microderms, and More!

It would be great to have something blooming. Flowers, or somehow make a woman look like she's blooming.

I am attaching a visual description of our special. However, the poster should NOT include the pricing tiers. I am also attaching our business logo. Thank you!!

Target Market(s)

A majority are women, but some are men. Around 25-55 in age. Middle to upper class who are likely to spend more money.

Industry/Entity Type

Medical

Font styles to use
Sans Serif
Script

Colors

Designer to choose colors to be used in the design.

Requirements
Must have
• Name of promotion: Marigold Jubilee
• Slogan: "Let Your Beauty Bloom"
• Concept "The more you buy, the more you save on your favorite spa services"
• Select from your favorite spa services such as NEVRIL, laser treatments, microderms, and more!
• Website: VerdaneSpaDeals.com
• Our logo (attached)
Nice to have
• Modern and creative design. Somehow tying in the "Let your beauty bloom" theme. We don't want the focus to be "The more you buy the more you save"
• We are looking for a unique design that is unlike traditional medical spas in the area that typically include a lot of white and a lot of overly photoshopped images.
• Creativity is key! Something that's different than just text and images. We would be so excited to see that!
Should not have
• Not too much text, but enough to get the point across.

```html
<!DOCTYPE html>
<html lang="en">
<head>
<meta charset="UTF-8">
<title>Marigold Jubilee – Verdane Clinical Spa</title>
<link rel="stylesheet" href="https://fonts.googleapis.com/css2?family=Pacifico&family=Great+Vibes&family=Roboto:wght@300;400;500;700&display=swap">
<style>
  :root {
    --page-bg: #ececec;
    --poster-pink: #f5c3d6;
    --poster-pink-deep: #ee9fbe;
    --poster-white: #fff7fa;
    --leaf-green: #3fae49;
    --leaf-green-dark: #2f8a36;
    --title-green-light: #7cc84a;
    --slate: #555a5e;
    --ink: #3c3f42;
    --rose-script: #d23a72;
    --rose-red: #e0485e;
    --rose-dark: #b52842;
    --skin: #efd6c8;
    --white: #ffffff;
  }
  * { box-sizing: border-box; margin: 0; padding: 0; }
  html, body {
    width: 1200px; height: 1140px; overflow: hidden;
    background: var(--page-bg);
  }
  .poster {
    position: absolute; left: 235px; top: 30px;
    width: 730px; height: 1080px;
    background:
      radial-gradient(ellipse 60% 45% at 48% 55%, var(--poster-white) 0%, rgba(255,247,250,0.6) 45%, rgba(255,247,250,0) 75%),
      linear-gradient(180deg, var(--poster-pink) 0%, #f8d3e1 50%, var(--poster-pink) 100%);
    overflow: hidden;
    font-family: "Roboto", Arial, sans-serif;
  }
  .poster__frame {
    position: absolute; inset: 10px;
    border: 2px solid rgba(255,255,255,0.85);
    pointer-events: none;
  }
  .blossom-branches {
    position: absolute; left: 0; top: 0; width: 730px; height: 170px;
    background: linear-gradient(180deg, rgba(238,159,190,0.75) 0%, rgba(245,195,214,0) 100%);
  }
  .blossom-corner {
    position: absolute; left: 0; bottom: 0; width: 150px; height: 260px;
    background: linear-gradient(20deg, rgba(238,159,190,0.7) 0%, rgba(245,195,214,0) 70%);
  }
  .title {
    position: absolute; left: 0; width: 100%; text-align: center;
  }
  .title__script {
    top: 78px;
    font-family: "Pacifico", cursive;
    font-size: 112px; line-height: 1;
    color: var(--leaf-green);
    background: linear-gradient(180deg, var(--title-green-light), var(--leaf-green-dark));
    -webkit-background-clip: text; background-clip: text;
    -webkit-text-fill-color: transparent;
    filter: drop-shadow(0 0 0 var(--white)) drop-shadow(2px 3px 0 rgba(255,255,255,0.9));
  }
  .title__sans {
    top: 238px;
    font-weight: 500; font-size: 66px; letter-spacing: 4px;
    color: var(--slate);
  }
  .slogan {
    position: absolute; left: 0; top: 318px; width: 100%; text-align: center;
    font-family: "Great Vibes", cursive; font-size: 36px;
    color: var(--rose-script);
  }
  .slogan-rule {
    position: absolute; left: 150px; top: 372px; width: 430px; height: 1px;
    background: rgba(210,58,114,0.35);
  }
  .model-photo {
    position: absolute; left: 90px; top: 405px; width: 310px; height: 400px;
    border-radius: 46% 46% 30% 30%;
    background: radial-gradient(ellipse at 50% 35%, var(--skin) 0%, #e9c5b4 45%, rgba(255,255,255,0.2) 80%, rgba(255,255,255,0) 100%);
  }
  .rose-photo {
    position: absolute; left: 88px; top: 745px; width: 250px; height: 240px;
    border-radius: 50%;
    background: radial-gradient(circle at 50% 42%, var(--rose-red) 0%, #d63c53 50%, var(--rose-dark) 85%, rgba(181,40,66,0) 100%);
  }
  .offer {
    position: absolute; right: 68px; top: 470px;
    text-align: right; font-size: 33px; line-height: 40px;
    text-transform: uppercase; font-weight: 400; color: var(--ink);
  }
  .offer__accent { color: var(--leaf-green); font-weight: 700; }
  .offer-rule {
    position: absolute; left: 460px; top: 642px; width: 210px; height: 1px;
    background: rgba(60,63,66,0.3);
  }
  .services {
    position: absolute; right: 68px; top: 668px;
    text-align: right; font-size: 25px; line-height: 35px;
    font-weight: 300; color: var(--ink);
  }
  .brand {
    position: absolute; right: 68px; top: 908px;
    display: flex; align-items: center; gap: 10px;
  }
  .brand__dot {
    width: 30px; height: 30px; border-radius: 50%;
    background: var(--leaf-green);
  }
  .brand__text { text-align: left; color: var(--slate); }
  .brand__name { font-size: 38px; line-height: 1; font-weight: 400; }
  .brand__sub { font-size: 10px; letter-spacing: 1px; margin-top: 4px; }
  .web-band {
    position: absolute; left: 10px; right: 10px; top: 1005px; height: 46px;
    background: var(--leaf-green);
    display: flex; align-items: center; justify-content: center;
    color: var(--white); font-size: 25px; letter-spacing: 3px; font-weight: 400;
  }
</style>
</head>
<body>
  <main class="poster">
    <div class="blossom-branches" role="img" aria-label="Pink cherry blossom branches along the top edge"></div>
    <div class="blossom-corner" role="img" aria-label="Soft pink blossom petals in the lower left corner"></div>

    <h1 class="title title__script">Marigold</h1>
    <div class="title title__sans">JUBILEE</div>
    <p class="slogan">Let Your Beauty Bloom</p>
    <div class="slogan-rule"></div>

    <div class="model-photo" role="img" aria-label="Photo of a smiling woman with long brown hair wrapped in a soft white towel"></div>
    <div class="rose-photo" role="img" aria-label="Photo of a large blooming red-pink camellia flower"></div>

    <p class="offer">
      The more<br>
      <span class="offer__accent">you buy</span><br>
      The more<br>
      <span class="offer__accent">you save</span>
    </p>
    <div class="offer-rule"></div>

    <p class="services">
      Choose from your<br>
      favorite spa services<br>
      NEVRIL,<br>
      Laser Treatments,<br>
      Microderms,<br>
      and More!
    </p>

    <div class="brand">
      <span class="brand__dot"></span>
      <div class="brand__text">
        <div class="brand__name">Verdane</div>
        <div class="brand__sub">MEDICAL CENTER &amp; CLINICAL SPA</div>
      </div>
    </div>

    <div class="web-band">VerdaneSpaDeals.com</div>
    <div class="poster__frame"></div>
  </main>
</body>
</html>
```